Crestline Lending Group Business Cards

We are looking to revamp the current business cards each of our locations uses. We are a lending company that specializes in personal loans, title loans, and tax services. We have locations in New Mexico, Texas, and Oklahoma.

We would like a cleaner, sleeker look while still highlighting what we offer. Title Loans, Personal Loans & Tax Services. We also want to include our referral fee somewhere on the card. We would like to see an English option as well as a Spanish option for the cards.

PLEASE NOTE: Some business cards do not include the employee's name but just the store's location, while others will include both.

These are double-sided business cards, and we would like to see proof if possible. I have included proofs of our current business cards for you to review below, as well as our company logo. Feel free to get creative with the logo, etc! Colors should match the logo; however, you do not need to use all of our logo colors if you don't want to.

```html
<!DOCTYPE html>
<html lang="es">
<head>
<meta charset="utf-8">
<title>Crestline Lending Group – Tarjetas de presentación</title>
<link href="https://fonts.googleapis.com/css2?family=Montserrat:wght@400;500;700;800&display=swap" rel="stylesheet">
<style>
  :root {
    --brand-green: #10522f;
    --brand-red: #c41e26;
    --fold-shadow: #1f2a22;
    --paper: #ffffff;
    --canvas: #ffffff;
  }
  * { margin: 0; padding: 0; box-sizing: border-box; }
  html, body {
    width: 1200px; height: 1000px; overflow: hidden;
    background: var(--canvas);
    font-family: "Montserrat", Arial, sans-serif;
  }
  .card {
    position: absolute;
    left: 311px;
    width: 555px; height: 320px;
    background: var(--paper);
    overflow: hidden;
  }
  .card--front { top: 138px; }
  .card--back  { top: 524px; }

  /* Front */
  .front__site {
    position: absolute; left: 0; width: 359px; top: 12px;
    text-align: center; color: var(--brand-red);
    font-weight: 700; font-size: 17px;
  }
  .front__brand-panel {
    position: absolute; right: 0; top: 0;
    width: 196px; height: 320px;
    background: var(--brand-green);
  }
  .front__brand-name {
    position: absolute; left: 98px; top: 160px;
    transform: translate(-50%, -50%) rotate(90deg);
    white-space: nowrap; text-align: center;
    color: var(--paper); font-weight: 700; font-size: 26px; line-height: 1.15;
  }
  .front__fold {
    position: absolute; left: 359px; top: 170px;
    width: 34px; height: 20px;
  }
  .front__ribbon {
    position: absolute; left: 0; top: 54px;
    width: 393px; height: 116px;
    background: var(--brand-red);
    padding: 12px 0 0 28px;
  }
  .front__headline {
    color: var(--paper); font-weight: 800;
    font-size: 44.5px; line-height: 45px; letter-spacing: 0.6px;
  }
  .front__offer-label {
    position: absolute; left: 40px; top: 192px;
    color: var(--brand-green); font-weight: 700; font-size: 27px;
  }
  .front__offer-amount {
    position: absolute; left: 38px; top: 214px;
    color: var(--brand-green); font-weight: 700;
    font-size: 86px; line-height: 1; letter-spacing: -3px;
  }

  /* Back */
  .back__contact {
    position: absolute; left: 0; top: 0;
    width: 359px; height: 119px;
    background: var(--brand-green);
    list-style: none; padding-top: 14px;
  }
  .back__contact li {
    display: flex; align-items: center;
    height: 29px; padding-left: 23px;
    color: var(--paper); font-size: 16.5px; font-weight: 400;
  }
  .back__contact svg { width: 22px; height: 22px; margin-right: 21px; flex: none; }
  .back__services {
    position: absolute; left: 0; top: 119px;
    width: 359px; height: 166px;
    background: var(--brand-red);
    list-style: none; padding-top: 29px;
  }
  .back__services li {
    display: flex; align-items: center;
    height: 33px; padding-left: 23px;
    color: var(--paper); font-size: 22px; font-weight: 700;
  }
  .back__services svg { width: 24px; height: 24px; margin-right: 20px; flex: none; }
  .back__person {
    position: absolute; left: 359px; top: 38px; width: 196px;
    text-align: center;
  }
  .back__name { color: var(--brand-red); font-weight: 800; font-size: 27.5px; line-height: 1; }
  .back__role { color: var(--brand-green); font-weight: 500; font-size: 16px; margin-top: 4px; }
  .back__brand-name {
    position: absolute; left: 359px; top: 170px; width: 196px;
    text-align: center; color: var(--brand-green);
    font-weight: 700; font-size: 21px; line-height: 1.2;
  }
  .back__address {
    position: absolute; left: 0; bottom: 0;
    width: 555px; height: 35px;
    background: var(--brand-green);
    color: var(--paper); font-size: 15.5px; font-weight: 500;
    display: flex; align-items: center; justify-content: center;
  }
</style>
</head>
<body>

<section class="card card--front" aria-label="Frente de la tarjeta">
  <p class="front__site">www.crestlinelending.com</p>
  <div class="front__brand-panel">
    <p class="front__brand-name">Crestline<br>Lending Group</p>
  </div>
  <svg class="front__fold" viewBox="0 0 34 20" aria-hidden="true">
    <polygon points="0,0 34,0 0,20" fill="var(--fold-shadow)"/>
  </svg>
  <div class="front__ribbon">
    <h1 class="front__headline">REFERIR A<br>UN AMIGO</h1>
  </div>
  <p class="front__offer-label">OBTENER HASTA</p>
  <p class="front__offer-amount">$100</p>
</section>

<section class="card card--back" aria-label="Reverso de la tarjeta">
  <ul class="back__contact">
    <li>
      <svg viewBox="0 0 24 24" aria-hidden="true"><path d="M6 20c0-8 5-14 12-15l1.5 3.5-3 1.5C13 11 11 14 10.5 18l-4.5 2z" fill="var(--paper)"/></svg>
      (505) 555-0148
    </li>
    <li>
      <svg viewBox="0 0 24 24" aria-hidden="true"><rect x="1" y="5" width="22" height="14" fill="var(--paper)"/><path d="M1 5l11 8 11-8" fill="none" stroke="var(--brand-green)" stroke-width="2"/></svg>
      abcde@crestlinelending.com
    </li>
    <li>
      <svg viewBox="0 0 24 24" aria-hidden="true" fill="none" stroke="var(--paper)" stroke-width="1.5"><circle cx="12" cy="12" r="10"/><ellipse cx="12" cy="12" rx="4.5" ry="10"/><path d="M2 12h20M4 6.5h16M4 17.5h16M12 2v20"/></svg>
      www.crestlinelending.com
    </li>
  </ul>

  <ul class="back__services">
    <li>
      <svg viewBox="0 0 24 24" aria-hidden="true" fill="none" stroke="var(--paper)" stroke-width="2.2"><path d="M20 8.5A10 10 0 1 1 16 3.5"/><path d="M7 11.5l4.5 4.5L22 4"/></svg>
      Préstamos sobre Títulos
    </li>
    <li>
      <svg viewBox="0 0 24 24" aria-hidden="true" fill="none" stroke="var(--paper)" stroke-width="2.2"><path d="M20 8.5A10 10 0 1 1 16 3.5"/><path d="M7 11.5l4.5 4.5L22 4"/></svg>
      Préstamos Personales
    </li>
    <li>
      <svg viewBox="0 0 24 24" aria-hidden="true" fill="none" stroke="var(--paper)" stroke-width="2.2"><path d="M20 8.5A10 10 0 1 1 16 3.5"/><path d="M7 11.5l4.5 4.5L22 4"/></svg>
      Servicios de Impuestos
    </li>
  </ul>

  <div class="back__person">
    <p class="back__name">Jane Doe</p>
    <p class="back__role">Gerente de Sucursal</p>
  </div>

  <p class="back__brand-name">Crestline<br>Lending Group</p>

  <p class="back__address">740 Juniper Avenue, Suite C, Pinebrook, Texas 75500</p>
</section>

</body>
</html>
```